Dermatology Clinic / Pediatric Clinic / Allergy Clinic

Its a school project so just make up all the information on the flyer.
i need "3 DIFFERENT FLYERS. All 8x12. Can be edited through Microsoft word.
DUE DATE: FRIDAY JUNE 10, 2016 NOT JUNE 22, 2016
First Name of the Project is: Dermatology Clinic,
Second Name of the Project is: Pediatric Clinic,
Last Name of the Project is: Allergy Clinic.
My professors instruction: A prospective client should be able to see your ad and know everything about the specialist and why they might need one. Be sure to utilize colors and pictures.
has accurate information on each flyers. Good knowledge of subject and presentation package well done.
flyer to advertise and promote service AND INFORMATION ON MY CHOSEN PROJECTS to help people gain more knowledge on each specialties.
ON THE FLYERS IT INCLUDE:
1) What services are offered
2) specialties of the clinic
3) Name of the doctor: Corinne Mae Delacruz
4) Address: Address: 415 Birchmere Rd. E. Suite 210, Toronto, ON M4K 2P7
5) Phone:(416) 555-0187
6) Clinic Hours:
(By appointment only)
Monday to Thursday: 8:30am – 3:30pm
Friday: 9:00am – 3:30pm
Saturday & Sunday: Close
and any other necessary information.
Updates
Target Market(s)
Deadline is on July 10, 2016
I dunno how to update the date. :( but it will be soon. July 10 Friday
Visual reminder for professionals working who can generate referrals. Friends and family who would like to purchase a gift certificate for friend/family member.
Pls help. Thank you
Industry/Entity Type
School
Requirements
Must have
- On the flyer it includes.
- 1) What services are offered
- 2) specialties of the clinic
- 3) Name of the doctor: Corinne Mae Delacruz
- 4) Address: Address: 415 Birchmere Rd. E. Suite 210, Toronto, ON M4K 2P7
- 5) Phone:(416) 555-0187
- and any other necessary information.
Nice to have
- made and can open and edit on Microsoft Word

```html
<!DOCTYPE html>
<html lang="en">
<head>
<meta charset="utf-8">
<title>Allergy Clinic Flyer</title>
<link rel="stylesheet" href="https://fonts.googleapis.com/css2?family=PT+Sans+Narrow:wght@700&family=Source+Sans+3:ital,wght@0,300;0,400;0,600;0,700;1,400&display=swap">
<style>
  :root {
    --page-bg: #e9e9ec;
    --sky: #1ab4ea;
    --sky-deep: #0596d8;
    --navy: #283891;
    --ink: #1a1a1a;
    --hours-blue: #1a6fbf;
    --white: #ffffff;
  }
  * { box-sizing: border-box; margin: 0; padding: 0; }
  html, body {
    width: 1200px; height: 1200px; overflow: hidden;
    background: var(--page-bg);
    font-family: "Source Sans 3", "Myriad Pro", sans-serif;
  }
  .flyer {
    position: absolute; left: 220px; top: 30px;
    width: 760px; height: 1140px;
    background: var(--white);
    overflow: hidden;
    box-shadow: 0 6px 24px rgba(0,0,0,.18);
  }
  .hero-photo {
    position: absolute; left: 0; top: 0; width: 760px; height: 381px;
    background:
      radial-gradient(ellipse 320px 300px at 560px 190px, #e2b08f 0%, #cf9473 45%, rgba(207,148,115,0) 75%),
      linear-gradient(90deg, #f2e53a 0%, #d7df45 30%, #a9c45a 52%, #c9a07d 72%, #b77d55 100%);
  }
  .headline {
    position: absolute; left: 43px; top: 104px;
    font-family: "PT Sans Narrow", "Myriad Pro Condensed", sans-serif;
    font-weight: 700; font-size: 62px; line-height: 65px;
    color: var(--white);
    text-shadow: 0 1px 3px rgba(0,0,0,.15);
  }
  .accent-band {
    position: absolute; left: 0; top: 381px; width: 760px; height: 42px;
    background: linear-gradient(90deg, var(--sky) 0%, #0aa7e6 70%, var(--sky-deep) 100%);
  }
  .brand {
    position: absolute; left: 0; top: 423px; width: 307px; height: 390px;
    text-align: center;
  }
  .brand-dot {
    width: 120px; height: 120px; border-radius: 50%;
    background: var(--sky);
    margin: 65px auto 0;
  }
  .brand-name {
    margin-top: 30px;
    font-weight: 600; font-size: 40px; line-height: 42px;
    letter-spacing: 1px;
    color: var(--navy);
  }
  .brand-address {
    margin: 10px auto 0; width: 200px;
    font-size: 15px; line-height: 20px; text-align: left;
    color: var(--navy);
  }
  .about-panel {
    position: absolute; left: 307px; top: 423px; width: 453px; height: 390px;
    background: var(--navy);
    padding: 46px 39px 0 28px;
    color: var(--white);
    font-weight: 300; font-size: 23px; line-height: 30px;
    text-align: justify;
  }
  .about-panel p + p { margin-top: 30px; }
  .about-panel strong { font-weight: 700; }
  .clinic-details {
    position: absolute; left: 33px; top: 845px;
    color: var(--ink);
  }
  .doctor-name { font-size: 29px; line-height: 36px; font-weight: 400; margin-bottom: 10px; }
  .hours-title { font-size: 22px; line-height: 28px; color: var(--hours-blue); }
  .hours-note { font-size: 22px; line-height: 28px; font-style: italic; }
  .hours-line { font-size: 22px; line-height: 28.5px; font-weight: 300; }
  .phone-band {
    position: absolute; left: 0; top: 1055px; width: 760px; height: 85px;
    background: linear-gradient(90deg, #2cc3f2 0%, var(--sky) 40%, var(--sky-deep) 100%);
    text-align: center;
  }
  .phone-number {
    font-weight: 700; font-size: 84px; line-height: 70px;
    color: var(--white); letter-spacing: 1px;
  }
</style>
</head>
<body>
  <main class="flyer">
    <div class="hero-photo" role="img" aria-label="Photo of a woman blowing her nose into a tissue against a blurred yellow spring meadow"></div>
    <h1 class="headline">Don’t Let<br>Alergy Slow<br>You Down</h1>
    <div class="accent-band"></div>

    <section class="brand">
      <div class="brand-dot"></div>
      <div class="brand-name">ALLERGY<br>CLINIC</div>
      <p class="brand-address">415 Birchmere Rd. E. Suite 210, Toronto, ON M4K 2P7</p>
    </section>

    <section class="about-panel">
      <p>Allergies range from the mild and transient to the chronic and disabling, in some patients they can be acute and life threatening.</p>
      <p>Corinne Mae Delacruz is committed to the provision of a <strong>high quality private sector diagnostic</strong> and <strong>management service</strong> for patients (adults and children) and referring doctors.</p>
    </section>

    <section class="clinic-details">
      <h2 class="doctor-name">Corinne Mae Delacruz, MD</h2>
      <p class="hours-title">Clinic Hours:</p>
      <p class="hours-note">(by appointment only)</p>
      <p class="hours-line">Monday to Thursday: 8:30am – 3:30pm</p>
      <p class="hours-line">Friday: 9:00am – 3:30pm</p>
      <p class="hours-line">Saturday &amp; Sunday: Close</p>
    </section>

    <div class="phone-band">
      <p class="phone-number">(416) 555-0187</p>
    </div>
  </main>
</body>
</html>
```